Non-Profit, Organic, Natural Feel, Clean & Simple Business Cards

Looking for a business card design. Has an organic, natural, new-age, clean and simple look/feel. We are a non-profit group that works with Moringa(a health plant/superfood) by spreading and sharing seeds of Moringa. A design that stands out but clean and professional. I will upload our new logo design. The font can be changed. Also I will upload some pictures of Moringa.
Our Facebook page is www.facebook.com/TulvaSproutTrust Check us out to get a feel of us.

Target Market(s)

Everyone. Movers & Shakers of The Sustainable, Natural Medicines & Cosmetics, Organic Food Farming Industry. And To The Common Person Or A Local Family.

Industry/Entity Type

Sustainability

Contact Information for Business Card

Email: TulvaSoilTrust@Brenwick.com
FB: www.Facebook.com/TulvaSproutTrust
Website: www.TulvaSproutTrust.com

Requirements
Must have
• Image/Pic/Design of Moringa Leaves. Somewhere on the card. Clean and Clear. So you could easily identify the Moringa from the Business Card. Something Alive, Living, Green Feel to the card design.
Nice to have
• A warm, friendly, professional feel to the design. A organic sustainable concept/future with Moringa is the business card impression/image we are trying to present.

```html
<!DOCTYPE html>
<html lang="en">
<head>
<meta charset="utf-8">
<title>Tulva Sprout Trust — Business Cards</title>
<link rel="stylesheet" href="https://fonts.googleapis.com/css2?family=Cinzel:wght@400;600&family=Open+Sans:wght@400&display=swap">
<style>
  :root {
    --page-bg: #e9e6df;
    --card-white: #ffffff;
    --brand-grey: #6f7270;
    --brand-green: #5aa83a;
    --green-light: #8fd11c;
    --green-mid: #6cbc12;
    --green-dark: #4e9a0c;
    --ink-white: #ffffff;
    --leaf-ghost: rgba(255, 255, 255, 0.16);
  }
  * { box-sizing: border-box; margin: 0; padding: 0; }
  html, body { width: 1200px; height: 843px; overflow: hidden; }
  body {
    background: var(--page-bg);
    display: flex;
    align-items: center;
    justify-content: center;
    gap: 48px;
    font-family: "Open Sans", Arial, sans-serif;
  }
  .card {
    width: 540px;
    height: 309px;
    border-radius: 22px;
    position: relative;
    overflow: hidden;
    box-shadow: 0 10px 28px rgba(0, 0, 0, 0.22);
  }
  /* Front */
  .card-front {
    background: var(--card-white);
    display: flex;
    align-items: center;
    justify-content: center;
  }
  .brand-lockup { display: flex; align-items: center; gap: 16px; }
  .brand-square {
    width: 54px; height: 54px;
    background: var(--brand-green);
  }
  .brand-name {
    font-family: "Cinzel", Georgia, serif;
    font-weight: 600;
    color: var(--brand-grey);
    font-size: 34px;
    line-height: 1.05;
    letter-spacing: 1px;
  }
  /* Back */
  .card-back {
    background: radial-gradient(ellipse at 55% 35%, var(--green-light) 0%, var(--green-mid) 55%, var(--green-dark) 100%);
    color: var(--ink-white);
  }
  .leaf-decoration {
    position: absolute;
    left: 300px; top: 40px;
    width: 150px; height: 250px;
    border-radius: 50% 50% 45% 45%;
    background: var(--leaf-ghost);
  }
  .back-brand {
    position: absolute;
    left: 34px; top: 34px;
    font-family: "Cinzel", Georgia, serif;
    font-weight: 600;
    font-size: 30px;
    line-height: 1.05;
    letter-spacing: 1px;
  }
  .contact-block {
    position: absolute;
    left: 250px; top: 150px;
    right: 24px;
  }
  .person-name {
    font-family: "Cinzel", Georgia, serif;
    font-size: 20px;
    letter-spacing: 1px;
  }
  .person-title {
    font-family: "Cinzel", Georgia, serif;
    font-size: 13px;
    letter-spacing: 1px;
    margin-bottom: 14px;
  }
  .contact-line {
    display: flex; align-items: center; gap: 9px;
    font-size: 12.5px;
    margin-bottom: 7px;
  }
  .contact-icon { width: 14px; height: 14px; flex: none; }
</style>
</head>
<body>
  <section class="card card-front" aria-label="Card front">
    <div class="brand-lockup">
      <div class="brand-square"></div>
      <div class="brand-name">Tulva Sprout<br>Trust</div>
    </div>
  </section>

  <section class="card card-back" aria-label="Card back">
    <div class="leaf-decoration" role="img" aria-label="Faint moringa leaf sprig decoration"></div>
    <div class="back-brand">Tulva Sprout<br>Trust</div>
    <div class="contact-block">
      <p class="person-name">Arlo Pennick</p>
      <p class="person-title">CEO/Founder</p>
      <p class="contact-line">
        <svg class="contact-icon" viewBox="0 0 14 14"><rect x="1" y="3" width="12" height="8" fill="none" stroke="#fff" stroke-width="1.3"/><path d="M1 3 L7 8 L13 3" fill="none" stroke="#fff" stroke-width="1.3"/></svg>
        TulvaSoilTrust@Brenwick.com
      </p>
      <p class="contact-line">
        <svg class="contact-icon" viewBox="0 0 14 14"><circle cx="7" cy="7" r="5.8" fill="none" stroke="#fff" stroke-width="1.3"/><ellipse cx="7" cy="7" rx="2.5" ry="5.8" fill="none" stroke="#fff" stroke-width="1"/><path d="M1.2 7 H12.8" stroke="#fff" stroke-width="1"/></svg>
        www.TulvaSproutTrust.com
      </p>
      <p class="contact-line">
        <svg class="contact-icon" viewBox="0 0 14 14"><rect x="1" y="1" width="12" height="12" fill="#fff"/></svg>
        /TulvaSproutTrust
      </p>
    </div>
  </section>
</body>
</html>
```